Brennick Drilling Inc. Business card design

Business card design for "Brennick Drilling Inc. - Directional Drilling Services"

Address is:

Brennick Drilling Inc.
512 - 73 Tarvel Crescent SW
Calgary, Alberta, Canada
T2K 4P8

Please incorporate the logo design into the card, thank you.

Target Market(s)

Oil & Gas and Drilling

Industry/Entity Type

Business

```html
<!DOCTYPE html>
<html lang="en">
<head>
<meta charset="utf-8">
<title>Brennick Drilling Inc. – Business Card</title>
<link rel="stylesheet" href="https://fonts.googleapis.com/css2?family=Source+Sans+3:wght@400;600&display=swap">
<style>
  :root {
    --brand-blue: #1f4b6e;
    --brand-blue-deep: #183d5a;
    --brand-blue-light: #2c5f86;
    --ink: #2b2f33;
    --rule: #2a5576;
    --paper: #ffffff;
    --backdrop: #e9ebee;
  }
  * { box-sizing: border-box; margin: 0; padding: 0; }
  html, body {
    width: 1200px; height: 1093px; overflow: hidden;
    background: var(--backdrop);
    font-family: "Source Sans 3", sans-serif;
  }
  .sheet {
    width: 1200px; height: 1093px;
    display: flex; flex-direction: column; align-items: center; justify-content: center;
    gap: 44px;
  }
  .card {
    width: 840px; height: 480px; position: relative;
    box-shadow: 0 6px 22px rgba(0,0,0,.18);
  }

  /* Front */
  .card--front {
    background: linear-gradient(100deg, var(--brand-blue-light) 0%, var(--brand-blue) 45%, var(--brand-blue-deep) 100%);
    color: var(--paper);
    display: flex; flex-direction: column; align-items: center; justify-content: center;
  }
  .front__mark {
    width: 150px; height: 150px; border-radius: 50%;
    background: var(--paper); margin-bottom: 26px;
  }
  .front__name {
    font-size: 58px; font-weight: 600; letter-spacing: -1px; line-height: 1;
  }
  .front__tagline {
    font-size: 31px; font-weight: 400; margin-top: 8px; opacity: .92;
  }

  /* Back */
  .card--back { background: var(--paper); color: var(--ink); }
  .back__brand {
    position: absolute; left: 46px; top: 46px;
    display: flex; align-items: center; gap: 18px;
  }
  .back__mark {
    width: 96px; height: 96px; border-radius: 50%; background: var(--brand-blue);
  }
  .back__name {
    font-size: 40px; font-weight: 600; color: var(--brand-blue-deep); line-height: 1; letter-spacing: -.5px;
  }
  .back__tagline {
    font-size: 22px; color: var(--brand-blue-light); margin-top: 4px;
  }
  .back__address {
    position: absolute; right: 46px; top: 46px;
    text-align: right; font-size: 18px; line-height: 1.3; color: var(--ink);
  }
  .back__rule {
    position: absolute; left: 150px; right: 46px; top: 170px;
    height: 2px; background: var(--rule);
  }
  .back__person {
    position: absolute; left: 46px; top: 236px;
    font-size: 34px; display: flex; align-items: center; gap: 14px;
  }
  .back__person .divider { width: 3px; height: 34px; background: var(--brand-blue); }
  .back__person .title { font-size: 24px; font-weight: 600; }
  .back__contacts {
    position: absolute; left: 46px; top: 300px;
    list-style: none; font-size: 20px; line-height: 1; color: var(--ink);
  }
  .back__contacts li { display: flex; align-items: center; gap: 12px; margin-bottom: 11px; }
  .back__contacts svg { width: 20px; height: 20px; fill: var(--brand-blue); flex: none; }
</style>
</head>
<body>
<main class="sheet">

  <section class="card card--front" aria-label="Card front">
    <div class="front__mark"></div>
    <h1 class="front__name">Brennick Drilling Inc.</h1>
    <p class="front__tagline">Directional Drilling Services</p>
  </section>

  <section class="card card--back" aria-label="Card back">
    <div class="back__brand">
      <div class="back__mark"></div>
      <div>
        <h2 class="back__name">Brennick Drilling Inc.</h2>
        <p class="back__tagline">Directional Drilling Services</p>
      </div>
    </div>

    <address class="back__address">
      Streetname 123<br>Zip/City<br>Country
    </address>

    <div class="back__rule"></div>

    <p class="back__person">
      <span class="name">Full name</span>
      <span class="divider"></span>
      <span class="title">Title</span>
    </p>

    <ul class="back__contacts">
      <li>
        <svg viewBox="0 0 20 20" aria-hidden="true"><path d="M4 2h4l2 5-2.5 1.5a11 11 0 0 0 4 4L13 10l5 2v4a2 2 0 0 1-2 2A14 14 0 0 1 2 4a2 2 0 0 1 2-2z"/></svg>
        0000 000 000
      </li>
      <li>
        <svg viewBox="0 0 20 20" aria-hidden="true"><path d="M6 1h8a1.5 1.5 0 0 1 1.5 1.5v15A1.5 1.5 0 0 1 14 19H6a1.5 1.5 0 0 1-1.5-1.5v-15A1.5 1.5 0 0 1 6 1zm.5 2.5v11h7v-11zM10 15.5a1 1 0 1 0 0 2 1 1 0 0 0 0-2z"/></svg>
        (00) 0000 0000
      </li>
      <li>
        <svg viewBox="0 0 20 20" aria-hidden="true"><path d="M2 4h16v12H2zm1.5 1.6V14.5h13V5.6L10 10.5z M3.8 5.5 10 9.2l6.2-3.7z"/></svg>
        support@BrennickDrillingInc.com
      </li>
      <li>
        <svg viewBox="0 0 20 20" aria-hidden="true"><path d="M10 1a9 9 0 1 0 0 18 9 9 0 0 0 0-18zm0 1.8c1 1.2 1.8 3 2 5.2H8c.2-2.2 1-4 2-5.2zM3 11h3.2c.1 2 .6 3.7 1.4 4.9A7.2 7.2 0 0 1 3 11zm0-2a7.2 7.2 0 0 1 4.6-4.9C6.8 5.3 6.3 7 6.2 9zm7 8.2c-1-1.2-1.8-3-2-5.2h4c-.2 2.2-1 4-2 5.2zm2.4-1.3c.8-1.2 1.3-2.9 1.4-4.9H17a7.2 7.2 0 0 1-4.6 4.9zM13.8 9c-.1-2-.6-3.7-1.4-4.9A7.2 7.2 0 0 1 17 9z"/></svg>
        www.BrennickDrillingInc.com
      </li>
    </ul>
  </section>

</main>
</body>
</html>
```